Business Card Design

It's an investment advisory service for individuals with all there investment needs. Also financial consulting to businesses and governmental agencies on retirement plans etc. It's personalized not commoditized help. Should show strength, knowledge and money orientation.

Industry/Entity Type

Investment

Contact Information for Business Card

B. Vel R. Financial Consulting and Wealth Management, Mirek Dale Hopstein, 5172 Paseo Las Colinas Verde, San Diego, CA 92084-6617, Registered Investment Advisor

Requirements
Nice to have
• Something money oriented

```html
<!DOCTYPE html>
<html lang="en">
<head>
<meta charset="utf-8">
<title>B. Vel R. Financial Consulting and Wealth Management — Business Card</title>
<link rel="stylesheet" href="https://fonts.googleapis.com/css2?family=Fira+Sans:wght@400;500;700&family=Roboto+Condensed:ital,wght@0,700;1,700&display=swap">
<style>
  :root {
    --page-bg: #e6e6e6;
    --card-lime: #a9cd26;
    --band-navy: #15203a;
    --logo-blue: #2e97dc;
    --text-navy: #1b2338;
    --text-dark: #2a3320;
    --coin-dark: #3b3414;
    --coin-gold: #8a7a2a;
    --divider: rgba(255,255,255,0.55);
  }
  html, body {
    margin: 0;
    width: 1200px;
    height: 1200px;
    overflow: hidden;
    background: var(--page-bg);
  }
  .business-card {
    position: absolute;
    left: 100px;
    top: 314px;
    width: 1000px;
    height: 571px;
    background: var(--card-lime);
    overflow: hidden;
    box-shadow: 0 10px 30px rgba(0,0,0,0.18);
    font-family: "Fira Sans", sans-serif;
  }
  .title-band {
    position: absolute;
    left: 90px;
    top: 60px;
    right: 0;
    height: 130px;
    background: var(--band-navy);
    display: flex;
    align-items: center;
  }
  .brand-mark {
    display: flex;
    align-items: center;
    gap: 12px;
    padding: 0 28px 0 28px;
  }
  .brand-dot {
    width: 22px;
    height: 22px;
    border-radius: 50%;
    background: var(--logo-blue);
  }
  .brand-name {
    font-family: "Fira Sans", sans-serif;
    font-weight: 700;
    font-size: 52px;
    color: var(--logo-blue);
    letter-spacing: -0.5px;
  }
  .firm-name {
    font-family: "Roboto Condensed", sans-serif;
    font-weight: 700;
    font-size: 40px;
    line-height: 1.05;
    color: var(--card-lime);
    margin: 0;
  }
  .advisor {
    position: absolute;
    left: 90px;
    top: 225px;
  }
  .advisor-name {
    margin: 0;
    font-weight: 700;
    font-size: 34px;
    color: var(--text-navy);
  }
  .advisor-title {
    margin: 4px 0 0;
    font-weight: 500;
    font-size: 21px;
    color: var(--text-dark);
  }
  .divider {
    position: absolute;
    left: 455px;
    top: 225px;
    width: 2px;
    height: 120px;
    background: var(--divider);
  }
  .contact {
    position: absolute;
    left: 485px;
    top: 222px;
    font-size: 26px;
    line-height: 1.25;
    color: var(--text-dark);
  }
  .contact p { margin: 0; }
  .contact-lines {
    display: flex;
    gap: 28px;
    margin-top: 6px !important;
    font-size: 22px;
  }
  .contact-item {
    display: flex;
    align-items: center;
    gap: 8px;
  }
  .contact-item svg { width: 22px; height: 22px; }
  .growth-illustration {
    position: absolute;
    left: 0;
    right: 0;
    bottom: 0;
    height: 200px;
    background: linear-gradient(to bottom, rgba(169,205,38,0) 0%, rgba(138,122,42,0.55) 45%, var(--coin-dark) 100%);
    clip-path: polygon(0 20%, 100% 75%, 100% 100%, 0 100%);
  }
</style>
</head>
<body>
  <section class="business-card">
    <header class="title-band">
      <div class="brand-mark">
        <span class="brand-dot"></span>
        <span class="brand-name">B. Vel R.</span>
      </div>
      <h1 class="firm-name">Financial Consulting and<br>Wealth Management</h1>
    </header>

    <div class="advisor">
      <p class="advisor-name">Mirek Dale Hopstein</p>
      <p class="advisor-title">Registered Investment Advisor</p>
    </div>

    <div class="divider"></div>

    <address class="contact" style="font-style:normal">
      <p>5172 Paseo Las Colinas Verde,</p>
      <p>San Diego, CA 92084-6617</p>
      <p class="contact-lines">
        <span class="contact-item">
          <svg viewBox="0 0 24 24" aria-hidden="true"><circle cx="12" cy="12" r="11" fill="#1b2338"/><path d="M8 6.5l2 0 1 3-1.5 1a7 7 0 0 0 4 4l1-1.5 3 1v2a1.5 1.5 0 0 1-1.5 1.5A10 10 0 0 1 6.5 8 1.5 1.5 0 0 1 8 6.5z" fill="#a9cd26"/></svg>
          (xxx) xxx-xxxx
        </span>
        <span class="contact-item">
          <svg viewBox="0 0 24 24" aria-hidden="true"><circle cx="12" cy="12" r="11" fill="#1b2338"/><rect x="8.5" y="5" width="7" height="14" rx="1.2" fill="none" stroke="#a9cd26" stroke-width="1.6"/><circle cx="12" cy="16.5" r="0.9" fill="#a9cd26"/></svg>
          xxxxxxxxxx
        </span>
      </p>
    </address>

    <div class="growth-illustration" role="img" aria-label="Illustration of stacked gold coins with green sprouts growing among them"></div>
  </section>
</body>
</html>
```